Flyer Design for Business: "Velvet Glow"

My Business name is "VELVET GLOW"

Laser Hair Removal
Non invasive and pain free
Look amazing and feel confident with a Hair Free body
Now is the time to start don't delay
1 treatment a month will ensure you are bikini hot for the summer months
Take full advantage of our OPENING SPECIALS of 30%-40% savings
Part payments available

CELLULITE & FAT REDUCTION
Now you too can look amazing without invasive surgery, downtime or discomfort
Tara Wellbrook & Monica Farrowdale are avid recipients of this treatment.
Effective on all skin types and delivers fast measurable results for:
Helping mums regain their pre-baby figures
Losing the love handles (but keeping the love)
Stretch mark reduction
Skin tightening
Cellulite busting on Arms, tummy, thighs.
Man boob reduction.
Latest technology:
Bi Polar radio frequency (RF)
infrared light
negative pressure (Vacuum)
Tissue manipulation through roller mechanical massage.
50% saving Call now

PDT LED REJUVENATION LIGHT THERAPY
ORVA Researchers found:
Fibroblast and muscles grew 5 times faster, stimulates
reconstruction of collagenous fibres of the dermis
These findings and more assist with:
Remove freckles, sunburn pigmentation,
Cures acne and hair follicle inflammation
Anti aging skin tightening
Reduces pore size
Improve the skin texture
Improves circulation
Red light : reduces pore size, softens skin wrinkles,reduces acne
Blue light: Kills the acne bacillus to eliminate acne, inhibit inflammation
Yellow light: Skin tightening, whitening and softens skin wrinkles
Purple light: combination of red & blue lights treats acne scars
Orange light increases cell energy and accelerates metabolism
$55 Saving and relax under the lights.

Who can resist a soothing Hot stone massage therapy after:
A hard stressful day at work
Aches and muscular pain

Pick anything from this info with a couple of nice images.

Target Market(s)

Females & males Sports minded people cyclists

Industry/Entity Type

Beauty Salon

Colors
00a990
e34197

Requirements
Must have
• a couple of images and
Nice to have
• Pink and bluey green like my business card

```html
<!DOCTYPE html>
<html lang="en">
<head>
<meta charset="utf-8">
<title>Velvet Glow – Opening Specials Flyer</title>
<link rel="stylesheet" href="https://fonts.googleapis.com/css2?family=Lobster+Two:ital,wght@1,700&family=Great+Vibes&family=Marcellus+SC&family=Tinos:wght@400;700&display=swap">
<style>
  :root {
    --pink: #e34197;
    --pink-deep: #b3156e;
    --pink-dark: #8e0f57;
    --teal: #00a990;
    --teal-light: #22c9b0;
    --teal-dark: #0a6f62;
    --peach: #f6d4c4;
    --peach-light: #fbe6dc;
    --plum: #4a0f2f;
    --script-pink: #c21d72;
    --ink: #10231f;
    --white: #ffffff;
  }
  * { margin: 0; padding: 0; box-sizing: border-box; }
  html, body { width: 907px; height: 1200px; overflow: hidden; background: #ffffff; }
  .flyer { position: relative; width: 907px; height: 1200px; overflow: hidden; background: var(--peach); font-family: "Tinos", "Times New Roman", serif; }
  .backdrop { position: absolute; inset: 0; }
  .portrait {
    position: absolute; left: 470px; top: 0; width: 437px; height: 500px;
    background: radial-gradient(ellipse at 55% 40%, #f1c7b2 0%, #e9b8a1 35%, #f4d2c2 70%, var(--peach) 100%);
  }
  .ribbon { position: absolute; left: 110px; top: 0; width: 214px; height: 196px; }
  .ribbon-text { position: absolute; left: 110px; top: 22px; width: 214px; text-align: center; color: var(--white); }
  .ribbon-title { font-family: "Marcellus SC", serif; font-size: 31px; line-height: 33px; letter-spacing: 1px; }
  .ribbon-rule { width: 160px; height: 2px; background: var(--white); margin: 7px auto 4px; }
  .ribbon-savings { font-family: "Great Vibes", cursive; font-size: 30px; line-height: 27px; }
  .brand { position: absolute; left: 130px; top: 190px; font-family: "Lobster Two", cursive; font-style: italic; font-weight: 700; font-size: 68px; color: var(--plum); letter-spacing: 1px; }
  .brand-rule { position: absolute; left: 130px; top: 283px; width: 420px; height: 2px; background: var(--plum); }
  .tagline { position: absolute; left: 130px; top: 290px; width: 420px; text-align: center; font-family: "Marcellus SC", serif; font-size: 19px; color: var(--plum); letter-spacing: 1px; }
  .promise { position: absolute; left: 0; top: 0; font-family: "Great Vibes", cursive; color: var(--script-pink); font-size: 36px; line-height: 1; }
  .promise span { position: absolute; white-space: nowrap; }
  .photo-circle { position: absolute; border-radius: 50%; border: 5px solid var(--pink-dark); box-shadow: 0 3px 8px rgba(0,0,0,.3); }
  .photo-arm { left: 451px; top: 291px; width: 196px; height: 196px; background: radial-gradient(circle at 40% 55%, #f3d0bd 0%, #e2ad93 55%, #c98c73 100%); }
  .photo-relax { left: 660px; top: 361px; width: 212px; height: 212px; background: radial-gradient(circle at 45% 60%, #f1cdb9 0%, #e5b9a2 45%, #f6f1ee 80%, #ffffff 100%); }
  .pill { position: absolute; height: 42px; border-radius: 21px; color: var(--white); font-family: "Marcellus SC", serif; font-size: 23px; line-height: 38px; text-align: center; letter-spacing: 1px; box-shadow: 0 3px 6px rgba(0,0,0,.35); font-weight: 400; }
  .pill-cellulite { left: 259px; top: 520px; width: 390px; background: linear-gradient(180deg, #ef4fa4, var(--pink-deep)); border: 2px solid #9d0f5d; }
  .pill-led { left: 194px; top: 889px; width: 520px; background: linear-gradient(180deg, #0f9c86, var(--teal-dark)); border: 2px solid #065a4f; }
  .copy { position: absolute; left: 32px; width: 843px; font-size: 16.5px; line-height: 21.5px; text-align: justify; }
  .copy-cellulite { top: 576px; color: var(--ink); }
  .copy-led { top: 952px; color: var(--white); }
  .bullets { position: absolute; list-style: none; font-size: 16.5px; line-height: 22px; }
  .bullets li { position: relative; padding-left: 22px; white-space: nowrap; }
  .bullets li::before { content: ""; position: absolute; left: 2px; top: 7px; width: 8px; height: 8px; border-radius: 50%; background: var(--white); }
  .results-a { left: 46px; top: 660px; color: var(--ink); }
  .results-b { left: 474px; top: 660px; color: var(--ink); }
  .tech-label { position: absolute; left: 32px; top: 744px; font-size: 16.5px; line-height: 22px; color: var(--ink); }
  .tech-list { left: 202px; top: 744px; color: var(--ink); }
  .lights { left: 46px; top: 1052px; color: var(--white); line-height: 21.5px; }
  .badge { position: absolute; border-radius: 50%; border: 4px solid var(--white); box-shadow: 0 4px 8px rgba(0,0,0,.35); text-align: center; color: var(--white); }
  .badge-saving { left: 688px; top: 736px; width: 132px; height: 132px; background: radial-gradient(circle at 40% 35%, #f25aae, var(--pink-deep)); }
  .badge-price { left: 684px; top: 1026px; width: 138px; height: 138px; background: radial-gradient(circle at 40% 35%, #3fd8c2, var(--teal)); color: #0c2e29; }
  .badge-big { font-family: "Tinos", serif; font-size: 42px; line-height: 42px; margin-top: 24px; }
  .badge-word { font-family: "Marcellus SC", serif; font-size: 19px; letter-spacing: 1px; line-height: 20px; }
  .badge-small { font-family: "Marcellus SC", serif; font-size: 13px; line-height: 14px; }
  .badge-price .badge-big { font-size: 54px; line-height: 54px; margin-top: 22px; }
  .badge-price .badge-small { font-size: 11.5px; line-height: 13px; }
</style>
</head>
<body>
<main class="flyer">
  <svg class="backdrop" width="907" height="1200" viewBox="0 0 907 1200" aria-hidden="true">
    <defs>
      <linearGradient id="tealFill" x1="0" y1="0" x2="1" y2="1">
        <stop offset="0" stop-color="#17b59c"/>
        <stop offset="0.5" stop-color="#33d1b8"/>
        <stop offset="1" stop-color="#00a990"/>
      </linearGradient>
      <linearGradient id="pinkFill" x1="0" y1="0" x2="0" y2="1">
        <stop offset="0" stop-color="#e34197"/>
        <stop offset="1" stop-color="#c8237f"/>
      </linearGradient>
      <linearGradient id="waveFill" x1="0" y1="0" x2="1" y2="0">
        <stop offset="0" stop-color="#e9e9e9"/>
        <stop offset="0.5" stop-color="#ffffff"/>
        <stop offset="1" stop-color="#f3f3f3"/>
      </linearGradient>
    </defs>
    <rect width="907" height="1200" fill="var(--peach)"/>
    <rect y="700" width="907" height="480" fill="url(#pinkFill)"/>
    <path d="M0,420 C250,420 520,520 907,470 L907,830 C650,905 300,905 0,800 Z" fill="url(#tealFill)"/>
    <path d="M0,800 C300,905 650,905 907,830" fill="none" stroke="#ffffff" stroke-width="4"/>
    <path d="M0,338 C220,318 420,370 600,470 L600,485 C420,385 220,336 0,356 Z" fill="var(--pink-deep)"/>
    <path d="M0,352 C220,332 420,384 596,480 C430,500 260,560 0,538 Z" fill="url(#waveFill)"/>
    <rect y="1180" width="907" height="20" fill="#ffffff"/>
  </svg>

  <div class="portrait" role="img" aria-label="Portrait of a smiling woman with glowing skin, hand resting against her cheek"></div>

  <svg class="ribbon" viewBox="0 0 214 196" aria-hidden="true">
    <rect x="0" y="0" width="214" height="14" fill="#8e0f57"/>
    <path d="M8,0 H206 V160 L107,196 L8,160 Z" fill="var(--pink)"/>
    <path d="M8,0 H206 V160 L107,196 L8,160 Z" fill="none" stroke="#9d0f5d" stroke-width="3"/>
  </svg>
  <div class="ribbon-text">
    <div class="ribbon-title">Opening<br>Specials</div>
    <div class="ribbon-rule"></div>
    <div class="ribbon-savings">30%-40%<br>savings</div>
  </div>

  <h1 class="brand">Velvet Glow</h1>
  <div class="brand-rule"></div>
  <p class="tagline">Non invasive and pain free</p>

  <p class="promise">
    <span style="left:42px;top:388px">Look amazing</span>
    <span style="left:168px;top:428px">&amp; feel confident with a</span>
    <span style="left:42px;top:470px">Hair Free Body</span>
  </p>

  <div class="photo-circle photo-arm" role="img" aria-label="Close-up of smooth bare arm and shoulder"></div>
  <div class="photo-circle photo-relax" role="img" aria-label="Woman relaxing with head resting on her folded arms"></div>

  <h2 class="pill pill-cellulite">Cellulite &amp; Fat Reduction</h2>
  <p class="copy copy-cellulite">Now you too can look amazing without invasive surgery, downtime or discomfort. Tara Wellbrook &amp; Monica Farrowdale are avid recipients of this treatment. Effective on all skin types and delivers fast measurable results for:</p>

  <ul class="bullets results-a">
    <li>Helping mums regain their pre-baby figures</li>
    <li>Losing the love handles (but keeping the love)</li>
    <li>Stretch mark reduction</li>
  </ul>
  <ul class="bullets results-b">
    <li>Skin tightening</li>
    <li>Cellulite busting on Arms, tummy, thighs.</li>
    <li>Man boob reduction.</li>
  </ul>

  <p class="tech-label">Latest technology:</p>
  <ul class="bullets tech-list">
    <li>Bi Polar radio frequency (RF)</li>
    <li>Infrared light</li>
    <li>Negative pressure (Vacuum)</li>
    <li>Tissue manipulation through roller mechanical massage</li>
  </ul>

  <div class="badge badge-saving">
    <div class="badge-big">50%</div>
    <div class="badge-word">Saving</div>
    <div class="badge-small">Call now</div>
  </div>

  <h2 class="pill pill-led">PDT LED Rejuvenation Light Therapy</h2>
  <p class="copy copy-led">ORVA Researchers found: Fibroblast and muscles grew 5 times faster, stimulates reconstruction of collagenous fibres of the dermis. These findings and more assist with: Remove freckles, sunburn pigmentation, Cures acne and hair follicle inflammation, Anti aging, skin tightening, Reduces pore size, Improve the skin texture, Improves circulation.</p>

  <ul class="bullets lights">
    <li>Red light : reduces pore size, softens skin wrinkles,reduces acne</li>
    <li>Blue light: Kills the acne bacillus to eliminate acne, inhibit inflammation</li>
    <li>Yellow light: Skin tightening, whitening and softens skin wrinkles</li>
    <li>Purple light: combination of red &amp; blue lights treats acne scars</li>
    <li>Orange light increases cell energy and accelerates metabolism</li>
  </ul>

  <div class="badge badge-price">
    <div class="badge-big">$55</div>
    <div class="badge-small">Saving &amp; relax<br>under the lights</div>
  </div>
</main>
</body>
</html>
```